I needed some business cards done for my band. We are a 9 piece funk/horn band that plays a lot of private parties, wedding receptions and music festivals. We'd like a design with vivid colors that incorporates our logo. You can check out our website at www.brasslanternband.example to see what type of vibe we are going for.

```html
<!DOCTYPE html>
<html lang="en">
<head>
<meta charset="utf-8">
<title>Brass Lantern — Business Cards</title>
<link href="https://fonts.googleapis.com/css2?family=Open+Sans:wght@400;700;800&display=swap" rel="stylesheet">
<style>
  :root {
    --lime: #c6dc30;
    --ink: #111111;
    --paper: #ffffff;
    --stage: #232323;
    --muted: #555555;
  }
  * { box-sizing: border-box; margin: 0; padding: 0; }
  html, body { width: 1200px; height: 780px; overflow: hidden; }
  body {
    background: var(--stage);
    font-family: "Open Sans", Arial, sans-serif;
    color: var(--ink);
    position: relative;
  }
  .card {
    position: absolute;
    top: 235px;
    width: 540px;
    height: 310px;
    border-radius: 22px;
    overflow: hidden;
    background: var(--lime);
  }
  .card--front { left: 40px; }
  .card--back { left: 620px; }
  .card__sweep { position: absolute; inset: 0; width: 100%; height: 100%; }

  /* Front */
  .front__name {
    position: absolute;
    left: 0; right: 0; top: 118px;
    text-align: center;
    font-weight: 800;
    font-size: 54px;
    letter-spacing: -1px;
    color: var(--lime);
  }

  /* Back */
  .back__mark {
    position: absolute;
    left: 58px; top: 92px;
    width: 150px; height: 150px;
    border-radius: 50%;
    background: var(--lime);
    display: flex; align-items: center; justify-content: center;
    text-align: center;
  }
  .back__mark-name {
    font-weight: 800;
    font-size: 22px;
    line-height: 1.1;
    color: var(--ink);
  }
  .back__divider {
    position: absolute;
    left: 236px; top: 78px;
    width: 1px; height: 150px;
    background: var(--ink);
  }
  .back__info { position: absolute; left: 262px; top: 70px; }
  .back__name { font-weight: 800; font-size: 28px; line-height: 1; }
  .back__name .accent { color: var(--lime); }
  .back__role { font-size: 13px; margin-top: 4px; }
  .contact { list-style: none; margin-top: 14px; }
  .contact__item {
    display: flex; align-items: center; gap: 8px;
    font-size: 12.5px; line-height: 1.55;
  }
  .contact__icon { width: 13px; height: 13px; flex: none; }
  .social {
    position: absolute;
    left: 262px; top: 248px;
    display: flex; align-items: center; gap: 8px;
    font-size: 14px;
  }
  .social__dot { width: 14px; height: 14px; border-radius: 50%; background: var(--lime); }
</style>
</head>
<body>

  <section class="card card--front" aria-label="Card front">
    <svg class="card__sweep" viewBox="0 0 540 310" preserveAspectRatio="none" aria-hidden="true">
      <ellipse cx="280" cy="150" rx="270" ry="235" transform="rotate(-18 280 150)" fill="var(--paper)"/>
    </svg>
    <div class="front__name">Brass Lantern</div>
  </section>

  <section class="card card--back" aria-label="Card back">
    <svg class="card__sweep" viewBox="0 0 540 310" preserveAspectRatio="none" aria-hidden="true">
      <ellipse cx="280" cy="150" rx="270" ry="235" transform="rotate(-18 280 150)" fill="var(--paper)"/>
    </svg>

    <div class="back__mark">
      <span class="back__mark-name">Brass<br>Lantern</span>
    </div>

    <div class="back__divider"></div>

    <div class="back__info">
      <h1 class="back__name"><span class="accent">Brass</span> Lantern</h1>
      <p class="back__role">Musician/Band</p>
      <ul class="contact">
        <li class="contact__item">
          <svg class="contact__icon" viewBox="0 0 16 16" aria-hidden="true"><path d="M3 1l3 3-1.5 2a9 9 0 0 0 5.5 5.5L12 10l3 3-2 2C7 15 1 9 1 3z" fill="var(--lime)"/></svg>
          555.014.2837
        </li>
        <li class="contact__item">
          <svg class="contact__icon" viewBox="0 0 16 16" aria-hidden="true"><circle cx="8" cy="8" r="7" fill="var(--lime)"/><path d="M1 8h14M8 1c3 3 3 11 0 14M8 1c-3 3-3 11 0 14" stroke="#fff" stroke-width="1" fill="none"/></svg>
          info@brasslanternband.example
        </li>
        <li class="contact__item">
          <svg class="contact__icon" viewBox="0 0 16 16" aria-hidden="true"><rect x="1" y="4" width="14" height="10" rx="1" fill="var(--lime)"/><path d="M1 5l7 5 7-5" stroke="#fff" stroke-width="1.2" fill="none"/></svg>
          www.brasslanternband.example
        </li>
      </ul>
    </div>

    <div class="social">
      <span class="social__dot" aria-hidden="true"></span>
      <span>Brasslanternband</span>
    </div>
  </section>

</body>
</html>
```